Packaging for coffee beans bag

looking for design for bags packaging for our coffee beans brand (logo attached) with special green color (you can select the best green color grade) for the sizes 1KG and 500GRAMS.
attached also pictures for our old packaging what we are looking to change.
attached the ai file for the final project.

```html
<!DOCTYPE html>
<html lang="en">
<head>
<meta charset="utf-8">
<title>Verdana House – Costa Rica Coffee Pouch</title>
<link rel="stylesheet" href="https://fonts.googleapis.com/css2?family=Montserrat:ital,wght@0,400;0,500;0,600;0,700;1,600&family=Roboto:ital,wght@0,400;0,500;0,700;0,900;1,400;1,700&display=swap">
<style>
  :root {
    --page: #f3f3f3;
    --pouch-dark: #0c544e;
    --pouch: #14665f;
    --pouch-light: #1f7a72;
    --ink: #0f4f49;
    --paper: #ffffff;
    --rule: #9fb6b3;
    --white: #ffffff;
  }
  * { box-sizing: border-box; margin: 0; padding: 0; }
  html, body { width: 1200px; height: 1042px; overflow: hidden; }
  body {
    background: var(--page);
    font-family: "Montserrat", sans-serif;
    position: relative;
  }

  .pouch {
    position: absolute;
    left: 380px; top: 130px;
    width: 440px; height: 780px;
    border-radius: 12px 12px 6px 6px;
    background: linear-gradient(100deg, var(--pouch-dark) 0%, var(--pouch) 40%, var(--pouch-light) 70%, var(--pouch) 100%);
    overflow: hidden;
    color: var(--white);
  }
  .pouch__artwork {
    position: absolute;
    left: 0; right: 0; top: 110px; bottom: 0;
    background:
      radial-gradient(ellipse at 20% 15%, rgba(255,255,255,0.08), transparent 45%),
      radial-gradient(ellipse at 85% 20%, rgba(255,255,255,0.07), transparent 40%),
      radial-gradient(ellipse at 50% 95%, rgba(255,255,255,0.08), transparent 45%);
  }

  .tear-strip {
    position: absolute;
    left: 0; right: 0; top: 42px;
    height: 30px;
    display: flex; align-items: center;
    font: 700 10px "Roboto", sans-serif;
    letter-spacing: 0.3px;
  }
  .tear-strip__tab { width: 30px; height: 26px; margin-left: 4px; }
  .tear-strip__label { margin: 0 12px 0 8px; }
  .tear-strip__arrows { display: flex; gap: 14px; }
  .tear-strip__arrows span {
    width: 0; height: 0;
    border-left: 8px solid var(--white);
    border-top: 4.5px solid transparent;
    border-bottom: 4.5px solid transparent;
  }

  .zipper {
    position: absolute;
    left: 0; right: 0; top: 94px;
    height: 8px;
    background:
      repeating-linear-gradient(90deg, var(--white) 0 4px, transparent 4px 8px) top / 100% 4px no-repeat,
      repeating-linear-gradient(90deg, transparent 0 4px, var(--white) 4px 8px) bottom / 100% 4px no-repeat;
  }
  .zipper__tag {
    position: absolute;
    left: 50%; top: -4px;
    transform: translateX(-50%);
    background: var(--pouch);
    border: 1px solid var(--white);
    border-radius: 4px;
    padding: 0 8px;
    font: 700 10px/14px "Roboto", sans-serif;
    letter-spacing: 1px;
  }

  .brand {
    position: absolute;
    left: 0; right: 0; top: 230px;
    display: flex; flex-direction: column; align-items: center;
  }
  .brand__dot {
    width: 58px; height: 58px;
    border-radius: 50%;
    background: var(--white);
    margin-bottom: 22px;
  }
  .brand__name { font: 600 34px/1 "Montserrat", sans-serif; letter-spacing: 1px; }

  .seal {
    position: absolute;
    left: 332px; top: 372px;
    width: 76px; height: 76px;
  }

  .label {
    position: absolute;
    left: 56px; top: 456px;
    width: 328px; height: 218px;
    background: var(--paper);
    color: var(--ink);
    padding: 12px 14px 10px;
  }
  .label::before, .label::after {
    content: "";
    position: absolute; left: 0; right: 0;
    height: 5px;
    background: linear-gradient(135deg, var(--pouch) 2.5px, transparent 2.6px) 0 0 / 5px 5px repeat-x,
                linear-gradient(225deg, var(--pouch) 2.5px, transparent 2.6px) 0 0 / 5px 5px repeat-x;
  }
  .label::before { top: 0; }
  .label::after { bottom: 0; transform: scaleY(-1); }

  .label__brand {
    display: flex; align-items: center; justify-content: center; gap: 8px;
    height: 22px;
    margin: 2px 0 6px;
  }
  .label__brand-dot { width: 16px; height: 16px; border-radius: 50%; background: var(--ink); }
  .label__brand-name { font: 600 14px/1 "Montserrat", sans-serif; letter-spacing: 0.5px; }

  .label__grid {
    display: grid;
    grid-template-columns: 112px 1fr;
    border-top: 1px solid var(--rule);
  }
  .label__cell { border-bottom: 1px solid var(--rule); }
  .label__cell--left { border-right: 1px solid var(--rule); }

  .tasting {
    font: italic 400 6.4px/1.35 "Roboto", sans-serif;
    text-align: center;
    padding: 5px 4px;
  }
  .origin-cell { display: flex; align-items: flex-start; padding: 4px 0 5px 8px; }
  .origin {
    flex: 1;
    background: var(--ink);
    color: var(--white);
    padding: 7px 6px 6px;
    text-align: center;
  }
  .origin__country { font: 900 19px/1 "Roboto", sans-serif; letter-spacing: 0.5px; }
  .origin__farm { font: 700 10px/1.2 "Roboto", sans-serif; letter-spacing: 0.4px; margin-top: 3px; }

  .row-tag { display: flex; align-items: stretch; height: 44px; }
  .row-tag__side {
    width: 12px;
    background: var(--ink);
    color: var(--white);
    font: 500 5.5px/12px "Roboto", sans-serif;
    writing-mode: vertical-rl;
    transform: rotate(180deg);
    text-align: center;
    letter-spacing: 0.5px;
  }
  .row-tag__side--outline { background: var(--white); color: var(--ink); border-left: 1px solid var(--rule); }
  .roast-cups { display: flex; align-items: center; justify-content: center; gap: 3px; flex: 1; }
  .notes {
    flex: 1;
    display: flex; align-items: center; justify-content: center;
    text-align: center;
    font: italic 700 11px/1.3 "Roboto", sans-serif;
  }

  .facts { font: 500 9.5px/1.3 "Roboto", sans-serif; padding: 6px 0 0 10px; }
  .facts b { font-weight: 900; }
  .facts--right { display: flex; justify-content: space-between; padding-left: 8px; }
  .weight { text-align: right; padding-right: 4px; }
  .weight__caption { font: 400 6px/1 "Roboto", sans-serif; margin-bottom: 8px; }
  .weight__value { font: 700 8.5px/1 "Roboto", sans-serif; }
</style>
</head>
<body>
  <main class="pouch">
    <div class="pouch__artwork" role="img" aria-label="Faint tonal illustration of coffee branches, blossoms and beans covering the pouch"></div>

    <div class="tear-strip">
      <svg class="tear-strip__tab" viewBox="0 0 30 26" aria-hidden="true">
        <path d="M1 5 H18 L28 13 L18 21 H1 Z" fill="none" stroke="#fff" stroke-width="1.6"/>
        <text x="11" y="16.5" text-anchor="middle" font-family="Roboto, sans-serif" font-size="8" font-weight="700" fill="#fff">TAB</text>
      </svg>
      <span class="tear-strip__label">PULL TAB TO OPEN</span>
      <div class="tear-strip__arrows">
        <span></span><span></span><span></span><span></span><span></span><span></span><span></span><span></span><span></span><span></span><span></span><span></span>
      </div>
    </div>

    <div class="zipper"><span class="zipper__tag">ZIPPER</span></div>

    <div class="brand">
      <span class="brand__dot"></span>
      <span class="brand__name">VERDANA HOUSE</span>
    </div>

    <svg class="seal" viewBox="0 0 80 80" aria-label="Best quality coffee">
      <defs><path id="sealArc" d="M12 52 A30 30 0 1 1 62 62"/></defs>
      <text font-family="Montserrat, sans-serif" font-size="7.5" letter-spacing="2.2" fill="#fff">
        <textPath href="#sealArc">BEST QUALITY COFFEE</textPath>
      </text>
    </svg>

    <section class="label">
      <div class="label__brand">
        <span class="label__brand-dot"></span>
        <span class="label__brand-name">VERDANA HOUSE</span>
      </div>

      <div class="label__grid">
        <p class="label__cell label__cell--left tasting">“Fruity Aroma, Long Sweet Finish, Structured Acidity, Juicy And Silky Mouthfeel, Flavour Note of Apricot, Caramel, Mixed Berries And Chocolate”</p>
        <div class="label__cell origin-cell">
          <div class="origin">
            <div class="origin__country">COSTA RICA</div>
            <div class="origin__farm">FINCA LOMAVERDE</div>
          </div>
        </div>

        <div class="label__cell label__cell--left row-tag">
          <span class="row-tag__side">ROAST</span>
          <div class="roast-cups">
            <svg width="26" height="24" viewBox="0 0 26 24" aria-hidden="true"><path d="M9 1 q2 2 0 4 M12 1 q2 2 0 4" stroke="#0f4f49" fill="none" stroke-width="0.8"/><path d="M3 8 H19 V14 a6 6 0 0 1 -6 6 H9 a6 6 0 0 1 -6 -6 Z" fill="#0f4f49"/><path d="M19 10 h2 a3 3 0 0 1 0 6 h-2" fill="none" stroke="#0f4f49" stroke-width="1.2"/><path d="M1 21 H21" stroke="#0f4f49"/></svg>
            <svg width="26" height="24" viewBox="0 0 26 24" aria-hidden="true"><path d="M3 8 H19 V14 a6 6 0 0 1 -6 6 H9 a6 6 0 0 1 -6 -6 Z" fill="none" stroke="#0f4f49" stroke-width="1.1"/><path d="M3 11 H19 V14 a6 6 0 0 1 -6 6 H9 a6 6 0 0 1 -6 -6 Z" fill="#0f4f49"/><path d="M19 10 h2 a3 3 0 0 1 0 6 h-2" fill="none" stroke="#0f4f49" stroke-width="1.2"/><path d="M1 21 H21" stroke="#0f4f49"/></svg>
            <svg width="26" height="24" viewBox="0 0 26 24" aria-hidden="true"><path d="M9 1 q2 2 0 4" stroke="#0f4f49" fill="none" stroke-width="0.8"/><path d="M3 8 H19 V14 a6 6 0 0 1 -6 6 H9 a6 6 0 0 1 -6 -6 Z" fill="none" stroke="#0f4f49" stroke-width="1.1"/><path d="M4 15 H18 a6 6 0 0 1 -5 5 H9 a6 6 0 0 1 -5 -5 Z" fill="#0f4f49"/><path d="M19 10 h2 a3 3 0 0 1 0 6 h-2" fill="none" stroke="#0f4f49" stroke-width="1.2"/><path d="M1 21 H21" stroke="#0f4f49"/></svg>
          </div>
        </div>
        <div class="label__cell row-tag">
          <span class="row-tag__side row-tag__side--outline">NOTES</span>
          <p class="notes">Mixed Berries And<br>Chocolate, Caramel</p>
        </div>

        <div class="facts">
          <b>Roasted</b> coffee<br><b>Whole</b> bean
        </div>
        <div class="facts facts--right">
          <div>Traditional<br>Natural<br>Method</div>
          <div class="weight">
            <div class="weight__caption">NET WEIGHT</div>
            <div class="weight__value">2.205 lb/1000 gr.</div>
          </div>
        </div>
      </div>
    </section>
  </main>
</body>
</html>
```